Postcard Design

Income tax servicesOver 20 years experienceBusiness and Personal Tax ReturnsAll State ReturnsFree Electronic FilingI would like a simple map showing how to get to my house.reasons to use a tax preparerYou don’t have to keep up with the many tax law changes or understand complicated tax law.Your time is worth money – add up the hours you would spend doing it yourself and calculate what that’s worth.A tax program in a box cannot represent you in an audit.A tax professional can answer your questions to help you make smarter tax-saving decisions.It gives you peace of mind knowing that a professional is taking care of it.It can save you money – if your tax preparer finds even one significant deduction or tax credit you may have missed, it can easily cover the cost to have them prepared.Going to be targeting the area within 2 square miles of my home office so would like to promote proximity to the possible clients
Electronic

```html
<!DOCTYPE html>
<html lang="en">
<head>
<meta charset="utf-8">
<title>Ultimate Tax Preparer Postcard</title>
<link href="https://fonts.googleapis.com/css2?family=Oswald:wght@500&family=Lato:wght@400;700&family=Roboto:wght@400;500&display=swap" rel="stylesheet">
<style>
  :root {
    --green: #6f8f2f;
    --green-light: #86a83c;
    --brown: #5b4a2c;
    --beige: #d8c9a2;
    --beige-light: #f1ebdc;
    --ink: #4d4d4d;
    --white: #ffffff;
    --stage: #e6e6e6;
  }
  * { margin: 0; padding: 0; box-sizing: border-box; }
  html, body { width: 806px; height: 1200px; overflow: hidden; }
  body { background: var(--stage); font-family: "Lato", sans-serif; position: relative; }

  .card { position: absolute; left: 44px; width: 718px; height: 516px; background: var(--white);
          box-shadow: 0 3px 8px rgba(0,0,0,.35); overflow: hidden; }
  .card--front { top: 59px; }
  .card--back { top: 625px; }
  .card__shapes { position: absolute; inset: 0; }

  /* front */
  .headline { position: absolute; left: 16px; top: 18px; }
  .headline__main { font-family: "Oswald", sans-serif; font-weight: 500; font-size: 50px; line-height: 1; color: var(--ink); letter-spacing: .5px; }
  .headline__sub { font-family: "Roboto", sans-serif; font-size: 29px; color: var(--green); margin-top: 4px; letter-spacing: .5px; }

  .benefits__tab { position: absolute; left: 14px; top: 151px; font-family: "Oswald", sans-serif; font-weight: 500;
                   font-size: 24px; color: var(--ink); letter-spacing: .5px; }
  .benefits__list { position: absolute; left: 18px; top: 192px; list-style: none; }
  .benefits__list li { color: var(--white); font-weight: 700; font-size: 15px; line-height: 18.5px; padding-left: 16px; position: relative; }
  .benefits__list li::before { content: ""; position: absolute; left: 0; top: 6px; width: 7px; height: 7px; border-radius: 50%; background: var(--white); }

  .call { position: absolute; left: 16px; top: 300px; font-weight: 700; font-size: 25px; color: var(--ink); }
  .call__label { color: var(--green); }

  .owner { position: absolute; left: 440px; width: 278px; top: 296px; text-align: center; }
  .owner__name { font-weight: 700; font-size: 44px; color: var(--ink); }
  .owner__firm { margin-top: 14px; font-weight: 700; font-size: 18px; color: var(--ink); display: inline-flex; align-items: center; gap: 8px; }
  .owner__firm::before { content: ""; width: 12px; height: 12px; border-radius: 50%; background: var(--ink); }

  .contact { position: absolute; list-style: none; }
  .contact li { color: var(--white); font-weight: 700; font-size: 14.5px; display: flex; align-items: center; gap: 9px; }
  .contact--front { left: 432px; top: 453px; }
  .contact--front li { line-height: 22px; }
  .contact--back { left: 18px; top: 484px; display: flex; gap: 16px; }
  .icon { width: 11px; height: 11px; flex: none; }

  /* back */
  .reasons-title { position: absolute; left: 22px; top: 12px; }
  .reasons-title__main { font-family: "Oswald", sans-serif; font-weight: 500; font-size: 29px; color: var(--green); line-height: 1.1; letter-spacing: .5px; }
  .reasons-title__sub { font-family: "Roboto", sans-serif; font-size: 23px; color: var(--ink); letter-spacing: .5px; }
  .reasons { position: absolute; left: 20px; top: 90px; width: 312px; list-style: none; display: flex; flex-direction: column; gap: 14px; }
  .reasons li { color: var(--white); font-weight: 700; font-size: 12.3px; line-height: 16px; padding-left: 16px; position: relative; text-align: justify; }
  .reasons li::before { content: ""; position: absolute; left: 0; top: 5px; width: 6px; height: 6px; border-radius: 50%; background: var(--white); }
</style>
</head>
<body>

<section class="card card--front">
  <svg class="card__shapes" viewBox="0 0 718 516" width="718" height="516">
    <defs>
      <linearGradient id="greenPanel" x1="0" y1="0" x2="1" y2="0">
        <stop offset="0" stop-color="#86a83c"/><stop offset="1" stop-color="#6a8a2c"/>
      </linearGradient>
      <linearGradient id="callBar" x1="0" y1="0" x2="1" y2="0">
        <stop offset="0" stop-color="#f1ebdc"/><stop offset="1" stop-color="#c9b88c"/>
      </linearGradient>
      <linearGradient id="coinPhoto" x1="0" y1="0" x2="1" y2="1">
        <stop offset="0" stop-color="#2c2f36"/><stop offset=".6" stop-color="#4a4c52"/><stop offset="1" stop-color="#a88a52"/>
      </linearGradient>
    </defs>
    <polygon points="262,0 300,0 352,276 718,276 718,290 340,290" fill="var(--green)"/>
    <polygon points="294,0 718,0 718,268 346,268" fill="url(#coinPhoto)" role="img" aria-label="Photo of a businessman in a suit arranging rising stacks of coins"/>
    <polyline points="0,136 306,136 480,484" fill="none" stroke="var(--brown)" stroke-width="7"/>
    <polygon points="0,145 298,145 470,490 0,490" fill="url(#greenPanel)"/>
    <polygon points="450,450 718,450 718,516 0,516 0,490 470,490" fill="var(--brown)"/>
    <polygon points="0,146 140,146 126,177 0,177" fill="var(--beige-light)"/>
    <polygon points="0,296 338,296 324,340 0,340" fill="url(#callBar)"/>
    <polygon points="0,380 322,380 298,456 0,456" fill="#ecebe6" stroke="var(--white)" stroke-width="3" role="img" aria-label="Street map showing the way to the home office"/>
  </svg>

  <header class="headline">
    <h1 class="headline__main">THE ULTIMATE</h1>
    <p class="headline__sub">TAX PREPARER</p>
  </header>

  <h2 class="benefits__tab">BENEFITS</h2>
  <ul class="benefits__list">
    <li>Over 20 years experience</li>
    <li>Business and Personal Tax Returns</li>
    <li>All State Returns</li>
    <li>Free Electronic Filing</li>
  </ul>

  <p class="call"><span class="call__label">Call now</span> 555-013-0142</p>

  <div class="owner">
    <p class="owner__name">Daniel Reed</p>
    <p class="owner__firm">Reed Tax Office</p>
  </div>

  <ul class="contact contact--front">
    <li><svg class="icon" viewBox="0 0 12 12"><rect x="0.5" y="2" width="11" height="8" fill="#9cbf4a"/><polyline points="0.5,2 6,7 11.5,2" fill="none" stroke="#5b4a2c" stroke-width="1"/></svg>reedtaxcpa@example.com</li>
    <li><svg class="icon" viewBox="0 0 12 12"><circle cx="6" cy="6" r="5.5" fill="#9cbf4a"/><path d="M0.5 6h11M6 .5v11" stroke="#5b4a2c" stroke-width="1"/></svg>www.cornerstreetcpa.com</li>
  </ul>
</section>

<section class="card card--back">
  <svg class="card__shapes" viewBox="0 0 718 516" width="718" height="516">
    <defs>
      <linearGradient id="greenBack" x1="0" y1="0" x2="1" y2="0">
        <stop offset="0" stop-color="#86a83c"/><stop offset="1" stop-color="#6a8a2c"/>
      </linearGradient>
      <linearGradient id="titleBand" x1="0" y1="0" x2="1" y2="0">
        <stop offset="0" stop-color="#f4efe2"/><stop offset="1" stop-color="#d3c298"/>
      </linearGradient>
      <linearGradient id="financePhoto" x1="0" y1="0" x2="1" y2="1">
        <stop offset="0" stop-color="#b77a4e"/><stop offset=".35" stop-color="#e9e6df"/><stop offset=".75" stop-color="#cfd3d8"/><stop offset="1" stop-color="#5f7ea6"/>
      </linearGradient>
    </defs>
    <rect x="0" y="0" width="430" height="470" fill="url(#greenBack)"/>
    <polygon points="0,0 420,0 400,76 0,76" fill="url(#titleBand)"/>
    <polygon points="0,470 420,470 410,516 0,516" fill="var(--brown)"/>
    <polygon points="412,0 426,0 366,516 352,516" fill="var(--beige)"/>
    <polygon points="426,0 718,0 718,516 366,516" fill="url(#financePhoto)" role="img" aria-label="Photo of coin stacks, a calculator and a pen on a financial newspaper"/>
  </svg>

  <header class="reasons-title">
    <h2 class="reasons-title__main">REASONS TO USE</h2>
    <p class="reasons-title__sub">A TAX PREPARER</p>
  </header>

  <ul class="reasons">
    <li>You don’t have to keep up with the many tax law changes or understand complicated tax law.</li>
    <li>Your time is worth money – add up the hours you would spend doing it yourself and calculate what that’s worth.</li>
    <li>A tax program in a box cannot represent you in an audit.</li>
    <li>A tax professional can answer your questions to help you make smarter tax-saving decisions.</li>
    <li>It gives you peace of mind knowing that a professional is taking care of it.</li>
    <li>It can save you money – if your tax preparer finds even one significant deduction or tax credit you may have missed, it can easily cover the cost to have them prepared.</li>
    <li>Going to be targeting the area within 2 square miles of my home office so would like to promote proximity to the possible clients</li>
  </ul>

  <ul class="contact contact--back">
    <li><svg class="icon" viewBox="0 0 12 12"><rect x="0.5" y="2" width="11" height="8" fill="#9cbf4a"/><polyline points="0.5,2 6,7 11.5,2" fill="none" stroke="#5b4a2c" stroke-width="1"/></svg>reedtaxcpa@example.com</li>
    <li><svg class="icon" viewBox="0 0 12 12"><circle cx="6" cy="6" r="5.5" fill="#9cbf4a"/><path d="M0.5 6h11M6 .5v11" stroke="#5b4a2c" stroke-width="1"/></svg>www.cornerstreetcpa.com</li>
  </ul>
</section>

</body>
</html>
```